Create a standard e-mail template for market research invitations.
Please follow attached layout.
E-mail template must be fully coded and uploaded to mailchimp account and fully tested before sign off.
Logos are uploaded. Our website is www.meetbrightwren.co.uk . Please stick to corporate image.
Example content:
Previous example attached. Happy with this style design or something a bit different, but must stick to layout style (html template 1 doc.) also attached. Template should allow for placement of similar content to given example and be text editable.
Main left hand side of header must be readable text and not downloadable image only to increase readership and improve look when arriving in inbox.
Thanks
Target Market(s)
General consumers
Industry/Entity Type
Market Research

```html
<!DOCTYPE html>
<html lang="en">
<head>
<meta charset="utf-8">
<title>Brightwren – Market Research Invitation</title>
<link href="https://fonts.googleapis.com/css2?family=Montserrat:wght@400;600;700&display=swap" rel="stylesheet">
<style>
  :root {
    --page-bg: #eeeeee;
    --brand-green: #93bd3b;
    --brand-brown: #7c6d62;
    --body-text: #857a71;
    --sky-top: #ffffff;
    --sky-mid: #c9d6ec;
    --sky-glow: #d6ecf6;
    --sky-bottom: #f4f6fa;
  }
  * { box-sizing: border-box; margin: 0; padding: 0; }
  html, body {
    width: 1200px; height: 1000px; overflow: hidden;
    background: var(--page-bg);
    font-family: "Montserrat", Arial, sans-serif;
  }
  .invite {
    position: absolute; left: 327px; top: 143px;
    width: 546px; height: 714px; overflow: hidden;
    background:
      radial-gradient(ellipse 180px 260px at 50% 52%, var(--sky-glow) 0%, rgba(214,236,246,0) 100%),
      linear-gradient(180deg, var(--sky-top) 0%, #eef2f8 22%, var(--sky-mid) 55%, #dfe6f2 78%, var(--sky-bottom) 100%);
    box-shadow: 0 2px 6px rgba(0,0,0,0.08);
  }
  .school-band { position: absolute; left: 0; top: 30px; width: 546px; height: 175px; }
  .brand-name {
    position: absolute; left: 362px; top: 74px;
    font-size: 29px; font-weight: 700; letter-spacing: -0.5px;
    color: var(--brand-brown);
  }
  .headline {
    position: absolute; left: 50px; top: 224px;
    font-size: 17px; font-weight: 700; color: var(--brand-green);
  }
  .subhead {
    position: absolute; left: 50px; top: 266px; width: 420px;
    font-size: 14.5px; font-weight: 700; line-height: 19px; color: var(--brand-brown);
  }
  .benefits {
    position: absolute; left: 90px; top: 345px; width: 420px;
    list-style: none;
  }
  .benefits li {
    position: relative; padding-left: 25px; margin-bottom: 19px;
    font-size: 12.5px; line-height: 23px; color: var(--body-text);
  }
  .benefits li::before {
    content: ""; position: absolute; left: 1px; top: 6px;
    width: 11px; height: 11px; border-radius: 50%;
    background: var(--brand-green);
  }
  .actions {
    position: absolute; left: 0; top: 572px; width: 546px;
    text-align: center; color: var(--brand-brown);
  }
  .actions a { color: var(--brand-brown); text-decoration: underline; text-underline-offset: 3px; font-weight: 700; }
  .register { display: block; font-size: 18.5px; line-height: 24px; }
  .faq { display: block; font-size: 13px; line-height: 22px; font-weight: 400; color: var(--body-text); }
  .site { display: block; font-size: 17.5px; line-height: 26px; }
  .footer-wave { position: absolute; left: 0; bottom: 0; width: 546px; height: 70px; }
</style>
</head>
<body>
  <main class="invite">
    <svg class="school-band" viewBox="0 0 546 175" role="img" aria-label="Decorative diagonal school of small green fish swimming across the header">
      <defs>
        <linearGradient id="schoolTone" x1="0" y1="0" x2="1" y2="1">
          <stop offset="0" stop-color="#93bd3b" stop-opacity="0.55"/>
          <stop offset="1" stop-color="#93bd3b" stop-opacity="0.35"/>
        </linearGradient>
      </defs>
      <path d="M0 10 C120 20 220 40 300 70 C380 100 460 110 546 115 L546 170 C460 160 390 150 300 125 C210 100 110 80 0 75 Z" fill="url(#schoolTone)"/>
    </svg>

    <div class="brand-name">brightwren</div>

    <h1 class="headline">Get paid for your beautiful opinions!</h1>
    <p class="subhead">Health and beauty companies need your expert opinions....</p>

    <ul class="benefits">
      <li>Invitations to participate in focus groups, telephone interviews and online surveys.</li>
      <li>Earn up to £100 for an hour of your time.</li>
      <li>Give your views on how companies innovate, launch, package and price their products.</li>
      <li>Thereis no cost to register and your privacy us gauranteed</li>
    </ul>

    <div class="actions">
      <a class="register" href="#">Click here to register</a>
      <span class="faq">FAQ's</span>
      <a class="site" href="#">www.meetbrightwren.co.uk</a>
    </div>

    <svg class="footer-wave" viewBox="0 0 546 70" preserveAspectRatio="none" aria-hidden="true">
      <path d="M0 38 C150 30 320 18 546 8 L546 70 L0 70 Z" fill="var(--brand-brown)"/>
      <path d="M0 44 C150 36 320 24 546 13 L546 70 L0 70 Z" fill="var(--brand-green)"/>
    </svg>
  </main>
</body>
</html>
```